Halvex Land Surveying Website Design

We are working with Halvex. They are a national land surveying company and in need of a new website design.

Some sites to use for inspiration:

https://brantholmeng.com
https://www.pvdinc.com
https://lurendo.com
https://gwy.us
https://korvanbuilt.com
https://www.ferrisgalbrandi.com

Thank you for taking the time to consider designing a website for us. We are web developers based in Stockton and Los Angeles, CA, USA. Most of our projects go through the same process. Understanding this process may help you win a project with us. We custom-code all of our websites in-house. We don’t have any requirements as to what tools you use for your design, but we prefer Figma files. For any design that we label as four-stars, we send it to the client for review. The client picks the final design they want us to use. Once we complete this process, we will continue to show additional clients all the four-star sites and purchase them later. Your designs will have multiple chances to sell. For better chances of success, we ask that you follow these guidelines.

IMAGES:
If you use any images or icons in the design, we ask that you have a link to the asset so we can purchase the image/icon. Most of the designs we submit do not have the customer’s images on them unless they have some great images. Be creative; show us the feeling you are trying to portray with your image choices. Use any royalty-free site you choose. We subscribe to Quillo and mainly use their images, but we can purchase images outside of Quillo.

PLEASE NOTE: we will not submit designs to clients with watermarks on the images.

FONTS:
We ask that you identify the fonts used in the design. This can be done in a message if you want. We typically use Vexmar Fonts and Quillo Fonts.

CONTENT:
We're always open to different content and ideas. We often submit designs with stock images so the client can see our vision. We typically take pictures after the website launch to use their images with our vision. Lorem Ipsum is fine for paragraphs, but we ask that you write the headers in correct English. We want to be able to show the vision and identify the sections of the website.

INSPIRATION:
We typically add a couple of links in the brief of websites we like to help you get started in your design.

REVISIONS:
We do not often ask for revisions of the designs unless we see something in the design that may not appeal to the client. If there are slight changes that we want to make, we do that in the development process.

FEEDBACK:
We rarely give feedback on designs during the design process. We are working on many website projects and do not have the time to provide feedback. We usually respond if your request is well thought out and asks specific questions, but a note asking “feedback, please” usually goes unanswered.

```html
<!DOCTYPE html>
<html lang="en">
<head>
<meta charset="utf-8">
<title>Halvex Land Surveying</title>
<link href="https://fonts.googleapis.com/css2?family=Russo+One&family=Oswald:wght@400;500&family=Lato:wght@400;700&display=swap" rel="stylesheet">
<style>
:root{
  --red:#d9261c;
  --dark:#262628;
  --ink:#111;
  --grey:#555;
  --pink:#fbe7e5;
  --white:#fff;
}
*{margin:0;padding:0;box-sizing:border-box}
html,body{width:1200px;height:3823px;overflow:hidden}
body{position:relative;background:var(--white);font-family:'Lato',sans-serif;color:var(--ink)}
.abs{position:absolute}
.display{font-family:'Russo One',sans-serif;font-weight:400}
.red{color:var(--red)}
.eyebrow{font-family:'Oswald',sans-serif;color:var(--grey);font-size:24px;letter-spacing:.5px;text-transform:uppercase}
.btn{position:absolute;background:var(--red);color:#fff;font-weight:700;border-radius:4px;display:flex;align-items:center;justify-content:center}

/* header */
.site-header{left:0;top:0;width:1200px;height:62px;background:#fff;z-index:5}
.brand{display:flex;align-items:center;gap:10px}
.brand-mark{width:34px;height:34px;border-radius:50%;background:var(--red)}
.brand-name{font-family:'Lato',sans-serif;font-weight:700;color:var(--red);font-size:26px}
.nav a{position:absolute;top:26px;font-size:15px;color:#222;text-decoration:none}
.nav a.active{top:21px;background:var(--red);color:#fff;padding:6px 10px;font-weight:700}

/* hero */
.hero{left:0;top:62px;width:1200px;height:600px;background:linear-gradient(180deg,#9fb1c2 0%,#b48a6a 35%,#8a5a3b 70%,#6f4630 100%)}
.hero-title{left:108px;top:160px;font-size:58px;line-height:66px;color:#fff}
.hero-lead{left:110px;top:362px;width:540px;color:#fff;font-size:15px;line-height:27px;font-weight:700}

/* services */
.service-card{top:830px;width:321px;height:398px;background:#fff;box-shadow:0 2px 8px rgba(0,0,0,.15)}
.service-card .photo{position:absolute;left:9px;top:10px;width:303px;height:332px}
.service-card .title{position:absolute;left:0;width:100%;text-align:center;font-size:20px;top:360px}
.service-card.active{border-bottom:6px solid var(--red);height:403px}
.service-card.active .photo{height:218px}
.service-card.active .badge{position:absolute;left:135px;top:196px;width:52px;height:52px;border-radius:50%;background:#fff}
.service-card.active .badge::after{content:"";position:absolute;left:16px;top:14px;width:20px;height:24px;background:var(--red);border-radius:4px}
.service-card.active .title{top:252px;color:var(--red);font-weight:700}
.service-card.active .text{position:absolute;top:290px;left:50px;width:221px;text-align:center;font-size:14px;line-height:23px;color:var(--grey)}

/* industries */
.serve{left:0;top:1335px;width:1200px;height:462px;background:linear-gradient(180deg,#d9392f,#c92a20)}
.industry{top:1513px;width:184px;height:213px;background:#fff;border-radius:92px 92px 0 0;text-align:center}
.industry .icon{width:104px;height:104px;border-radius:50%;background:#6b6b6b;margin:21px auto 0}
.industry.active .icon{background:var(--red)}
.industry .label{margin-top:22px;font-size:20px;line-height:25px;text-transform:uppercase}

/* about */
.stat-box{left:111px;top:1820px;width:387px;height:470px;background:var(--pink)}
.stat-num{font-family:'Russo One',sans-serif;color:var(--red);font-size:54px}
.stat-label{font-size:22px;color:#444}
.about-text{left:741px;top:2018px;width:350px;font-size:14px;line-height:32px;color:var(--grey);text-align:justify}

/* testimonials */
.review .avatar{width:56px;height:56px;border-radius:50%;background:#d7d0cb}
.review .name{font-size:18px}
.stars{color:#f5b800;font-size:14px;letter-spacing:1px}
.review .quote{font-size:13px;line-height:27px;color:var(--grey)}

/* footer */
.footer h4{font-size:21px;font-weight:400;color:#fff}
.footer ul{list-style:none}
.footer li{font-size:15px;color:#fff;height:33px}
.footer .contact{color:#fff;font-size:15px;display:flex;align-items:center;gap:14px}
.pin{width:22px;height:22px;border-radius:50%;background:#fff}
.social span{display:inline-block;width:30px;height:30px;border-radius:50%;background:#fff;margin-right:4px}
.social span.on{background:var(--red)}
</style>
</head>
<body>

<header class="abs site-header">
  <div class="abs brand" style="left:108px;top:14px"><span class="brand-mark"></span><span class="brand-name">HALVEX</span></div>
  <nav class="nav">
    <a class="active" href="#" style="left:445px">Home</a>
    <a href="#" style="left:535px">About Us</a>
    <a href="#" style="left:638px">Services</a>
    <a href="#" style="left:732px">Projects</a>
    <a href="#" style="left:820px">Resources</a>
  </nav>
  <svg class="abs" style="left:946px;top:23px" width="20" height="20" viewBox="0 0 20 20"><circle cx="8" cy="8" r="6.5" fill="none" stroke="#333" stroke-width="1.6"/><line x1="13" y1="13" x2="18" y2="18" stroke="#333" stroke-width="1.6"/></svg>
  <div class="btn" style="left:998px;top:12px;width:89px;height:40px;font-size:15px">Contact</div>
</header>

<section class="abs hero" role="img" aria-label="Construction site with a surveying level on a tripod under a cloudy sky"></section>
<h1 class="abs hero-title display">Precision in Every<br><span class="red">Measurement Trust</span><br>Across the Nation</h1>
<p class="abs hero-lead">Halvex delivers accurate, reliable, and on-time land surveying services for developers, engineers, architects, and property owners nationwide.</p>
<div class="btn" style="left:112px;top:431px;width:140px;height:38px;font-size:15px">Request a Quote</div>
<svg class="abs" style="left:0;top:530px" width="1200" height="140" viewBox="0 0 1200 140">
  <path d="M0 20 Q600 200 1200 15 L1200 140 L0 140Z" fill="#fff"/>
  <path d="M0 20 Q600 200 1200 15" fill="none" stroke="#d9261c" stroke-width="6"/>
</svg>

<h2 class="abs display" style="left:0;width:1200px;text-align:center;top:725px;font-size:44px">What <span class="red">We Do</span></h2>
<div class="abs eyebrow" style="left:0;width:1200px;text-align:center;top:782px">Services</div>

<article class="abs service-card" style="left:111px">
  <div class="photo" role="img" aria-label="Aerial view of green farmland plots marked with boundary pins" style="background:linear-gradient(160deg,#3f6e2a,#8fbf4a 55%,#2f5522)"></div>
  <div class="title">Land &amp; Boundary Surveys</div>
</article>
<article class="abs service-card active" style="left:443px">
  <div class="photo" role="img" aria-label="Construction workers in hard hats reviewing a site" style="background:linear-gradient(160deg,#cfd6dc,#b9b3a4 60%,#8c8474)"></div>
  <div class="badge"></div>
  <div class="title">Construction Staking</div>
  <div class="text">Accurate layout services to guide contractors and ensure projects are built to plan.</div>
</article>
<article class="abs service-card" style="left:776px">
  <div class="photo" role="img" aria-label="Two surveyors with plans and a tripod at a quarry" style="background:linear-gradient(180deg,#4a90cf,#9cc6e6 40%,#c9a877 62%,#b08a55)"></div>
  <div class="title">Topographic &amp; Mapping</div>
</article>

<section class="abs serve" role="img" aria-label="Survey crew at a construction site, tinted red"></section>
<h2 class="abs display" style="left:0;width:1200px;text-align:center;top:1378px;font-size:44px;color:#fff">Who We Serve</h2>
<div class="abs eyebrow" style="left:0;width:1200px;text-align:center;top:1442px;color:#fff">Industries</div>

<div class="abs industry" style="left:114px"><div class="icon"></div><div class="label">Developers</div></div>
<div class="abs industry" style="left:312px"><div class="icon"></div><div class="label">Engineers</div></div>
<div class="abs industry active" style="left:509px"><div class="icon"></div><div class="label">Architects</div></div>
<div class="abs industry" style="left:706px"><div class="icon"></div><div class="label">Government<br>Agencies</div></div>
<div class="abs industry" style="left:903px"><div class="icon"></div><div class="label">Homeowners</div></div>

<div class="abs stat-box"></div>
<div class="abs stat-num" style="left:163px;top:1884px">20+</div>
<div class="abs stat-label" style="left:137px;top:1958px">Years in Business</div>
<div class="abs stat-num" style="left:163px;top:2021px">50</div>
<div class="abs stat-label" style="left:132px;top:2095px">States Covered</div>
<div class="abs stat-num" style="left:163px;top:2166px">10+</div>
<div class="abs stat-label" style="left:132px;top:2240px">Industries Served</div>
<div class="abs" role="img" aria-label="Surveyor in a hard hat and safety vest using a total station" style="left:328px;top:1903px;width:376px;height:430px;background:linear-gradient(160deg,#8a7f70,#b9a98c 40%,#c9d23a 70%,#6d6354)"></div>

<h2 class="abs display" style="left:733px;top:1895px;font-size:52px">Who <span class="red">We Are</span></h2>
<div class="abs eyebrow" style="left:741px;top:1968px">About Us</div>
<p class="abs about-text">Halvex is a national land surveying company dedicated to delivering accurate, reliable, and timely surveying solutions for clients across the United States. With a reputation built on precision and trust, we serve developers, engineers, architects, contractors, government agencies, and property owners who rely on us to bring clarity to every project.</p>
<div class="btn" style="left:740px;top:2272px;width:108px;height:41px;font-size:15px">Read More</div>

<h2 class="abs display" style="left:0;width:1200px;text-align:center;top:2415px;font-size:44px">Our <span class="red">Projects</span></h2>
<div class="abs eyebrow" style="left:0;width:1200px;text-align:center;top:2473px">Work</div>
<div class="abs" role="img" aria-label="Aerial view of a large retail building and parking lot surrounded by trees" style="left:0;top:2530px;width:600px;height:414px;background:linear-gradient(160deg,#6d8a3e,#b7bcb8 45%,#7f8a84 70%,#56703a)"></div>
<div class="abs" role="img" aria-label="Aerial view of a data center campus among green fields" style="left:605px;top:2530px;width:595px;height:414px;background:linear-gradient(170deg,#8aa0ad,#5f7d45 30%,#9da7a6 55%,#5a7a3e)"></div>
<div class="abs" style="left:30px;top:2742px;width:20px;height:20px;border-radius:50%;background:#fff"></div>
<div class="abs" style="left:1136px;top:2742px;width:20px;height:20px;border-radius:50%;background:#fff"></div>

<h2 class="abs display" style="left:111px;top:3022px;font-size:44px">Client <span class="red">Testimonials</span></h2>
<div class="abs eyebrow" style="left:111px;top:3081px">Reviews</div>
<div class="abs" style="left:1051px;top:3037px;width:15px;height:15px;border-radius:50%;background:var(--red)"></div>
<div class="abs" style="left:1075px;top:3037px;width:15px;height:15px;border-radius:50%;background:#aaa"></div>

<div class="abs review" style="left:111px;top:3158px;width:400px">
  <div class="abs avatar" style="left:6px;top:0" role="img" aria-label="Client portrait"></div>
  <div class="abs name" style="left:83px;top:10px">Maren L</div>
  <div class="abs stars" style="left:83px;top:36px">★★★★★</div>
  <p class="abs quote" style="left:0;top:94px;width:400px">“Halvex’s survey team was precise, efficient, and communicative throughout our entire commercial development project. Highly recommended!”</p>
</div>
<div class="abs" style="left:596px;top:3180px;height:140px;border-left:2px dashed #bbb"></div>
<div class="abs review" style="left:642px;top:3158px;width:430px">
  <div class="abs avatar" style="left:6px;top:0" role="img" aria-label="Client portrait"></div>
  <div class="abs name" style="left:86px;top:10px">Teodor V</div>
  <div class="abs stars" style="left:83px;top:36px">★★★★★</div>
  <p class="abs quote" style="left:0;top:94px;width:430px">“Their construction staking services saved us time and prevented costly errors. Halvex’s professionalism is unmatched.”</p>
</div>

<svg class="abs" style="left:0;top:3410px" width="1200" height="413" viewBox="0 0 1200 413">
  <path d="M0 100 Q600 -40 1200 100 L1200 413 L0 413Z" fill="#262628"/>
  <path d="M0 92 Q600 -50 1200 92" fill="none" stroke="#d9261c" stroke-width="6"/>
</svg>
<footer class="abs footer" style="left:0;top:3410px;width:1200px;height:413px">
  <div class="abs brand" style="left:111px;top:130px"><span class="brand-mark" style="width:44px;height:44px"></span><span class="brand-name" style="font-size:36px">HALVEX</span></div>
  <div class="abs" style="left:111px;top:234px;width:326px;height:47px;background:#fff;border-radius:4px;font-size:12px;color:#666;padding:15px 20px">Enter Email Address</div>
  <div class="btn" style="left:111px;top:305px;width:132px;height:40px;font-size:17px">Subscribe</div>

  <h4 class="abs" style="left:495px;top:120px">Quick Links</h4>
  <ul class="abs" style="left:498px;top:164px"><li>Home</li><li>About Us</li><li>Services</li><li>Events</li><li>Media</li><li>Contact Us</li></ul>
  <h4 class="abs" style="left:657px;top:120px">Other Links</h4>
  <ul class="abs" style="left:661px;top:164px"><li>Privacy Policy</li><li>Terms &amp; Conditions</li><li>Disclaimer</li><li>FAQ’s</li><li>Support</li><li>Help</li></ul>
  <h4 class="abs" style="left:868px;top:120px">Contact Info</h4>
  <div class="abs contact" style="left:868px;top:164px"><span class="pin"></span>Lorem Ipsum, USA -437916</div>
  <div class="abs contact" style="left:868px;top:219px"><span class="pin"></span>+1 555 014 2290</div>
  <div class="abs contact" style="left:868px;top:273px"><span class="pin"></span>info@halvexlandsurveying.com</div>
  <div class="abs social" style="left:902px;top:327px" aria-label="Social links"><span class="on"></span><span></span><span></span><span></span><span></span></div>
  <div class="abs" style="left:111px;top:372px;width:978px;border-top:1px solid #888"></div>
  <div class="abs" style="left:0;width:1200px;text-align:center;top:386px;color:#fff;font-size:14px">© 2025 Halvex Land Surveying.All rights reserved</div>
</footer>

</body>
</html>
```